Book Title: Lantern Seasons -- Unwritten Pages of a Quiet Vocation

I am looking for just the book cover design, do not need spine or back cover art.

This book is a memoir and the cover needs to be prepared for print and ebook applications.

The part of the title that follows the dash ("Unwritten Pages of a Quiet Vocation") is not a subtitle but a tag and can be separated from the title itself.

I am inclined to a traditional design with "modern and minimalist" tendencies. I like graphic images that convey the idea of a "journey" or "quest". The memoir is about my pastoral work as a Christian minister but it is not a "religious" book. I do not want churches or any traditional religious symbols on the cover. In fact this book is directed toward those who have little, if any, interest in organized religion of any kind and if that could somehow be captured in the cover art it would be useful.

I am attaching a file with some sample cover art designs that I like or do not like to help guide your thinking. I am open to your interpretation and creative thinking. This book is a labor of love and I want the cover art to reflect my deep thinking on the topic.

```html
<!DOCTYPE html>
<html lang="en">
<head>
<meta charset="utf-8">
<title>Lantern Seasons — Book Cover</title>
<link rel="stylesheet" href="https://fonts.googleapis.com/css2?family=Cinzel:wght@500;600&family=Montserrat:wght@700&display=swap">
<style>
  :root {
    --paper: #f7f8f8;
    --ink-navy: #001428;
    --tag-sand: #b0a68a;
    --sky-light: #c0e1ea;
    --sky-band: #a0d0de;
    --shore-slate: #5b6d7c;
    --water-teal: #3c9fb5;
    --water-deep: #4f6b7d;
    --water-pale: #a9d6e4;
    --foam: #ffffff;
  }
  * { margin: 0; padding: 0; box-sizing: border-box; }
  html, body { width: 800px; height: 1200px; overflow: hidden; background: var(--paper); }
  .cover {
    position: relative;
    width: 800px;
    height: 1200px;
    background: var(--paper);
    overflow: hidden;
  }
  .title {
    position: absolute;
    left: 0; right: 0;
    top: 46px;
    text-align: center;
    font-family: "Cinzel", serif;
    font-weight: 600;
    color: var(--ink-navy);
    text-transform: uppercase;
    line-height: 1;
  }
  .title-line-top {
    display: block;
    font-size: 90px;
    letter-spacing: 0.24em;
    margin-right: -0.24em;
  }
  .title-line-main {
    display: block;
    margin-top: 4px;
    font-size: 136px;
    letter-spacing: 0.04em;
    margin-right: -0.04em;
  }
  .tagline {
    position: absolute;
    left: 0; right: 0;
    top: 311px;
    text-align: center;
    font-family: "Cinzel", serif;
    font-weight: 500;
    font-size: 38px;
    line-height: 0.92;
    letter-spacing: 0.14em;
    text-transform: uppercase;
    color: var(--tag-sand);
  }
  .tagline span { display: block; margin-right: -0.14em; }
  .scene-art {
    position: absolute;
    left: 0;
    top: 420px;
    width: 800px;
    height: 700px;
    display: block;
  }
  .author {
    position: absolute;
    left: 0; right: 0;
    top: 1137px;
    text-align: center;
    font-family: "Montserrat", sans-serif;
    font-weight: 700;
    font-size: 34px;
    letter-spacing: 0.5em;
    margin-right: -0.5em;
    text-transform: uppercase;
    color: var(--ink-navy);
    line-height: 1;
  }
</style>
</head>
<body>
  <main class="cover">
    <h1 class="title">
      <span class="title-line-top">Lantern</span>
      <span class="title-line-main">Seasons</span>
    </h1>
    <p class="tagline">
      <span>Unwritten Pages of a</span>
      <span>Quiet Vocation</span>
    </p>

    <svg class="scene-art" viewBox="0 0 800 700" role="img" aria-label="Posterised illustration of a white sailboat under full sail crossing a choppy blue lake beneath a pale sky with small clouds and a dark wooded shoreline">
      <path class="sky-band" d="M0 70 Q150 40 300 30 T560 12 T800 40 V700 H0 Z" fill="var(--sky-band)"/>
      <path class="sky" d="M0 110 Q200 80 400 72 T800 70 V700 H0 Z" fill="var(--sky-light)"/>
      <path class="shoreline" d="M0 305 L300 312 L520 318 L700 300 L800 298 V355 H0 Z" fill="var(--shore-slate)"/>
      <rect class="water-near" x="0" y="352" width="800" height="120" fill="var(--water-teal)"/>
      <rect class="water-mid" x="0" y="472" width="800" height="90" fill="var(--water-deep)"/>
      <rect class="water-foam" x="0" y="562" width="800" height="80" fill="var(--water-pale)"/>
      <path class="water-edge" d="M0 642 H800 V680 Q600 700 400 690 T0 684 Z" fill="var(--foam)"/>
    </svg>

    <p class="author">Author Name</p>
  </main>
</body>
</html>
```